Jetzt starten So funktioniert'sAuf die Visitenkarte soll ein Logo bzw. eine Grafik dargestellt werden, welche ebenfalls auf der Website und dem Flyer genutzt werden soll wird es hier als Logo bezeichnet. Die Grafik soll ein Labyrinth und eine Person in einer scheinbar aussichtsloser Lage darstellen mit der Frage „WANDEL gefä..
16Stein, Weg, Füße, Baby o. Kind....Sonne... Vielleicht fällt Ihnen auch etwas besseres ein. Evtl. ein Slogan wie z. B. -Kinderbetreuung mit ❤️ - Hier steht das Kind im Mittelpunkt. -Jedes Kind ist einzigartig? Oder - „Hilf mir es selbst zu tun“ aber vielleicht anders formuliert. (..
40Es müssen für zwei Geschäfte Visitenkarten, Briefpapier (A4) und Kassenkassenbelege (A6) erstellt werden. Logo und Typo im Anhang. Ein Farbkonzept besteht noch nicht. Die Idee geht in Richtung Bordeaux-Rot. Generell: (1) Sieht erstmal nach viel Beschreibung aus, bitte nicht entmutigen lass..
118Schlichtes aber direkt erkennbares Design. Koch dir Kraft , Gesundheit und Ernährungsberatung ( gut lesbar , elegant) Marlene Obrist-Kähler ( nicht so groß ) Grau ; Grün Töne und gerne etwas rosa Infos wie Adresse und E-Mail vielleicht in jeweilige Blöcke am unteren Rand
30Wir benötigen, passend zu unserem neuen Logo, Geschäftspapier, Visitenkarten und eine Vorlage für eine PowerPoint Präsentation (Hintergrunds-Seite)

```html
<!DOCTYPE html>
<html lang="de">
<head>
<meta charset="utf-8">
<title>Visitenkarte Jonas Berthold</title>
<link href="https://fonts.googleapis.com/css2?family=Fira+Sans:wght@400;700&display=swap" rel="stylesheet">
<style>
  :root {
    --page: #ffffff;
    --card-light-a: #e2e2e2;
    --card-light-b: #f7f7f7;
    --band: #6b7fa4;
    --navy: #0d3568;
    --band-text: #ffffff;
  }
  * { margin: 0; padding: 0; box-sizing: border-box; }
  html, body {
    width: 1200px; height: 1022px; overflow: hidden;
    background: var(--page);
    font-family: "Fira Sans", sans-serif;
  }
  .business-card {
    position: absolute; left: 150px; top: 220px;
    width: 900px; height: 582px;
    background: linear-gradient(90deg, var(--card-light-a), var(--card-light-b));
    box-shadow: 0 10px 40px rgba(0,0,0,0.18);
    overflow: hidden;
  }
  .brand {
    position: absolute; left: 70px; top: 70px;
    width: 240px; display: flex; flex-direction: column; align-items: center;
  }
  .brand-dot {
    width: 170px; height: 170px; border-radius: 50%;
    background: var(--navy);
  }
  .brand-name {
    margin-top: 18px; font-size: 34px; font-weight: 700;
    color: var(--navy); letter-spacing: 0.02em;
  }
  .person {
    position: absolute; left: 360px; top: 88px;
  }
  .person-name {
    font-size: 46px; font-weight: 700; color: var(--navy);
    text-transform: uppercase; letter-spacing: 0.04em;
  }
  .services { list-style: none; margin-top: 22px; }
  .services li {
    display: flex; align-items: center; gap: 14px;
    font-size: 31px; color: var(--navy); letter-spacing: 0.03em;
    margin-bottom: 14px;
  }
  .services svg { width: 14px; height: 18px; flex: none; }
  .contact-band {
    position: absolute; left: 0; bottom: 0; width: 100%; height: 200px;
    background: var(--band);
    padding: 52px 0 0 90px;
    color: var(--band-text); font-size: 30px; line-height: 1.35;
    letter-spacing: 0.04em;
  }
</style>
</head>
<body>
  <section class="business-card">
    <div class="brand">
      <div class="brand-dot"></div>
      <div class="brand-name">Textwerk</div>
    </div>
    <div class="person">
      <h1 class="person-name">Jonas Berthold</h1>
      <ul class="services">
        <li><svg viewBox="0 0 14 18"><path d="M2 2 L11 9 L2 16" fill="none" stroke="#0d3568" stroke-width="4"/></svg>Korrektorat</li>
        <li><svg viewBox="0 0 14 18"><path d="M2 2 L11 9 L2 16" fill="none" stroke="#0d3568" stroke-width="4"/></svg>Textredaktion</li>
        <li><svg viewBox="0 0 14 18"><path d="M2 2 L11 9 L2 16" fill="none" stroke="#0d3568" stroke-width="4"/></svg>Ghostwriting</li>
      </ul>
    </div>
    <footer class="contact-band">
      <p class="address">Lindenweg 7, 25336 Elmshorn</p>
      <p class="phone-mail">Tel. (0 41 21) 47 29 018, j.berthold@textpost.de</p>
    </footer>
  </section>
</body>
</html>
```